Brenmoor Group needs a business card

I would like the card to be simple but modern and elegant.
I like black and white.
or black and gold.
we are a private finance lender and also are involved in property and property developments.

please look at the business card photos i provided i would like B.G only one one side and all the other details on the other side use fonts that tie in with my theme.

Industry/Entity Type

Finance

Contact Information for Business Card

Brenmoor Group (B.G) Callum Brenmoor M: 0418396152 E: callumbren@quivomail.com

Font styles to use
Other font styles liked:
• Use fonts that would reflect our business

Colors
000000
ffffff

Requirements
Must have
• one side of details
• other side has either B.G or Brenmoor Group like in the photos provided

```html
<!DOCTYPE html>
<html lang="en">
<head>
<meta charset="UTF-8">
<title>Brenmoor Group – Business Card</title>
<link href="https://fonts.googleapis.com/css2?family=Cinzel:wght@500&family=Open+Sans:wght@400;700&display=swap" rel="stylesheet">
<style>
  :root {
    --backdrop: #3b3431;
    --card-black: #0d0d0d;
    --gold: #d6a51f;
    --white: #f2f2f2;
  }
  html, body {
    margin: 0;
    padding: 0;
    width: 1200px;
    height: 844px;
    overflow: hidden;
    background: var(--backdrop);
  }
  .stage {
    position: relative;
    width: 1200px;
    height: 844px;
  }
  .card {
    position: absolute;
    top: 272px;
    width: 520px;
    height: 300px;
    background: var(--card-black);
    box-shadow: 0 10px 30px rgba(0,0,0,0.45);
  }
  .card--details { left: 55px; }
  .card--brand { left: 625px; }

  .brand {
    position: absolute;
    display: flex;
    flex-direction: column;
    align-items: center;
  }
  .brand__square {
    border: 3px solid var(--gold);
    box-sizing: border-box;
  }
  .brand__name {
    font-family: "Cinzel", serif;
    font-weight: 500;
    color: var(--gold);
    letter-spacing: 0.04em;
    white-space: nowrap;
  }

  .card--details .brand { right: 38px; top: 34px; }
  .card--details .brand__square { width: 104px; height: 104px; margin-bottom: 12px; }
  .card--details .brand__name { font-size: 19px; }

  .card--brand .brand { left: 50%; top: 62px; transform: translateX(-50%); }
  .card--brand .brand__square { width: 120px; height: 120px; margin-bottom: 14px; }
  .card--brand .brand__name { font-size: 21px; }

  .contact {
    position: absolute;
    right: 38px;
    top: 190px;
    margin: 0;
    padding: 0;
    list-style: none;
    font-family: "Open Sans", sans-serif;
    font-size: 13px;
    color: var(--white);
    text-align: right;
  }
  .contact__item {
    display: flex;
    justify-content: flex-end;
    align-items: center;
    gap: 8px;
    margin-bottom: 14px;
  }
  .contact__icon { width: 12px; height: 12px; fill: var(--gold); }

  .person-name {
    position: absolute;
    left: 34px;
    bottom: 40px;
    margin: 0;
    font-family: "Open Sans", sans-serif;
    font-weight: 700;
    font-size: 19px;
    color: var(--gold);
  }
</style>
</head>
<body>
<main class="stage">

  <section class="card card--details" aria-label="Business card, details side">
    <div class="brand">
      <div class="brand__square"></div>
      <span class="brand__name">Brenmoor Group</span>
    </div>
    <ul class="contact">
      <li class="contact__item">
        <span>0418396152</span>
        <svg class="contact__icon" viewBox="0 0 24 24" aria-hidden="true"><path d="M6.6 10.8a15.1 15.1 0 0 0 6.6 6.6l2.2-2.2a1 1 0 0 1 1-.25 11.4 11.4 0 0 0 3.6.57 1 1 0 0 1 1 1V20a1 1 0 0 1-1 1A17 17 0 0 1 3 4a1 1 0 0 1 1-1h3.5a1 1 0 0 1 1 1c0 1.25.2 2.45.57 3.57a1 1 0 0 1-.25 1z"/></svg>
      </li>
      <li class="contact__item">
        <span>callumbren@quivomail.com</span>
        <svg class="contact__icon" viewBox="0 0 24 24" aria-hidden="true"><path d="M2 5h20v14H2z" fill="none"/><path d="M2 5h20v2l-10 6L2 7zM2 9l10 6 10-6v10H2z"/></svg>
      </li>
    </ul>
    <p class="person-name">Callum Brenmoor</p>
  </section>

  <section class="card card--brand" aria-label="Business card, brand side">
    <div class="brand">
      <div class="brand__square"></div>
      <span class="brand__name">Brenmoor Group</span>
    </div>
  </section>

</main>
</body>
</html>
```